"The Volmeret" - Horror Film Poster

Design a unique Modern Horror Film Poster for a film titled THE VOLMERET from TALLBROOK PICTURES. The film is being shot in March on a micro budget in London, UK.

Who or What is The Volmeret? - The Volmeret is an OLD and EVIL Female Ghost.

The Volmeret is a woman in her fifties who is from yje 1940's war era!

SHE WAS BRICKED UP BEHIND AND OLD FASHOINED FIREPLACE - IDEA: GHOST COMING OUT OF FIREPLACE OR HAND COMING OUT FOR BRICKED UP FIREPLACE

The design will be used as part of our promo packages and will be recreated on T-Shirts, Mugs, Key rings, websites, Posters.

MUST HAVE:

Tag Line:
She has been waiting...

Main Title:
Darren P. Okafor's
The Volmeret

THE VOLMERET is the OLDER WOMAN FROM THE 1940'S

Target Market(s)

12 - 40 Age group

Industry/Entity Type

Entertainment

Requirements
Must have
• Tag Line:
She has been waiting...

Main Title:
Darren P. Okafor's
The Volmeret

All in font - "Stone Serif SC ITC TT"
(uploaded for you)
Nice to have
• SHE WAS BRICKED UP BEHIND AND OLD FASHOINED FIREPLACE

Perhaps a fireplace with her coming through it with light behind!

```html
<!DOCTYPE html>
<html lang="en">
<head>
<meta charset="utf-8">
<title>The Volmeret – Poster</title>
<link rel="stylesheet" href="https://fonts.googleapis.com/css2?family=Cormorant+SC:wght@500;600;700&family=EB+Garamond:wght@500;600&display=swap">
<style>
  :root {
    --bg: #262626;
    --bg-dark: #1b1b1b;
    --frame: #f2f2f2;
    --white: #f4f4f4;
    --red: #b0474c;
    --tag-red: rgba(168, 64, 70, 0.86);
    --studio-green: #4fd14a;
    --photo-light: #f1f1f1;
    --photo-mid: #9a9a9a;
    --photo-dark: #3a3a3a;
  }
  * { margin: 0; padding: 0; box-sizing: border-box; }
  html, body { width: 840px; height: 1200px; overflow: hidden; background: var(--bg-dark); }
  .poster {
    position: relative;
    width: 840px;
    height: 1200px;
    overflow: hidden;
    background:
      repeating-linear-gradient(45deg, rgba(255,255,255,0.025) 0 1px, transparent 1px 4px),
      repeating-linear-gradient(-45deg, rgba(0,0,0,0.08) 0 1px, transparent 1px 5px),
      radial-gradient(ellipse at 50% 45%, #2c2c2c 0%, var(--bg) 55%, var(--bg-dark) 100%);
  }
  .poster-frame {
    position: absolute;
    inset: 16px;
    border: 5px solid var(--frame);
  }
  .presenter {
    position: absolute;
    top: 56px;
    width: 100%;
    text-align: center;
    font-family: "EB Garamond", serif;
    font-weight: 500;
    color: var(--white);
    font-size: 32px;
    line-height: 1;
    letter-spacing: 0.5px;
  }
  .presents {
    position: absolute;
    top: 100px;
    width: 100%;
    text-align: center;
    font-family: "EB Garamond", serif;
    font-weight: 600;
    color: var(--red);
    font-size: 30px;
    line-height: 1;
    letter-spacing: 0.5px;
  }
  .ghost-portrait {
    position: absolute;
    left: 236px;
    top: 218px;
    width: 420px;
    height: 664px;
    background:
      radial-gradient(ellipse 70px 50px at 76% 8%, rgba(230,230,230,0.85) 0%, rgba(230,230,230,0) 100%),
      radial-gradient(ellipse 110px 250px at 48% 70%, var(--photo-light) 0%, #d6d6d6 45%, rgba(214,214,214,0) 100%),
      radial-gradient(ellipse 120px 150px at 62% 42%, #dcdcdc 0%, rgba(200,200,200,0) 100%),
      radial-gradient(ellipse 90px 200px at 14% 45%, rgba(120,120,120,0.55) 0%, rgba(90,90,90,0) 100%),
      radial-gradient(ellipse 190px 300px at 46% 52%, var(--photo-mid) 0%, var(--photo-dark) 60%, rgba(38,38,38,0) 100%);
  }
  .tagline {
    position: absolute;
    left: 0;
    top: 0;
    width: 840px;
    height: 1200px;
  }
  .tagline text {
    font-family: "Cormorant SC", serif;
    font-weight: 600;
    fill: var(--tag-red);
  }
  .credit {
    position: absolute;
    top: 910px;
    width: 100%;
    text-align: center;
    font-family: "Cormorant SC", serif;
    font-weight: 700;
    color: var(--red);
    font-size: 38px;
    line-height: 1;
  }
  .film-title {
    position: absolute;
    top: 946px;
    width: 100%;
    text-align: center;
    font-family: "Cormorant SC", serif;
    font-weight: 700;
    color: var(--white);
    font-size: 108px;
    line-height: 1.1;
    letter-spacing: 2px;
  }
  .studio-mark {
    position: absolute;
    top: 1122px;
    width: 100%;
    text-align: center;
    font-family: "Cormorant SC", serif;
    font-weight: 700;
    color: var(--studio-green);
    font-size: 22px;
    line-height: 1;
    letter-spacing: 1px;
  }
</style>
</head>
<body>
  <main class="poster">
    <div class="poster-frame"></div>

    <p class="presenter">TALLBROOK PICTURES</p>
    <p class="presents">PRESENTS</p>

    <div class="ghost-portrait" role="img" aria-label="Black and white photograph of the pale ghost woman with dark hair and black eyes emerging from the darkness"></div>

    <svg class="tagline" viewBox="0 0 840 1200" aria-label="She's been waiting">
      <text x="74" y="406" font-size="258" textLength="706" lengthAdjust="spacingAndGlyphs">SHE’S</text>
      <text x="74" y="636" font-size="236" textLength="706" lengthAdjust="spacingAndGlyphs">BEEN</text>
      <text x="78" y="816" font-size="170" textLength="700" lengthAdjust="spacingAndGlyphs">WAITING</text>
    </svg>

    <p class="credit">Darren P. Okafor's</p>
    <h1 class="film-title">The Volmeret</h1>

    <p class="studio-mark">TALLBROOK PICTURES</p>
  </main>
</body>
</html>
```